Ridgeback Gear Depot

Design a new website design for www.ridgebackgeardepot.example,

Target Market(s)

Men & Ladies

Industry/Entity Type

Side X side, ATV Offroad

Coding

Coded - Design and coding required

Number of Pages Required

1 page

```html
<!DOCTYPE html>
<html lang="en">
<head>
<meta charset="utf-8">
<title>Ridgeback Gear Depot</title>
<link href="https://fonts.googleapis.com/css2?family=Poppins:wght@400;500;600;700&family=Playfair+Display:wght@500;600&display=swap" rel="stylesheet">
<style>
:root{
  --ink:#111111;
  --black:#0b0b0b;
  --white:#ffffff;
  --paper:#f1f1f1;
  --line:#d9d9d9;
  --muted:#555555;
  --star:#f2a516;
  --heart:#d7263d;
  --footer-text:#e6e6e6;
}
*{box-sizing:border-box;margin:0;padding:0}
html,body{width:1200px;height:3684px;overflow:hidden}
body{font-family:"Poppins",sans-serif;color:var(--ink);background:var(--white);position:relative}
a{color:inherit;text-decoration:none}

/* header */
.site-header{height:112px;background:var(--black);display:flex;align-items:center;padding:0 64px 0 88px;color:var(--white)}
.brand{font-weight:700;font-size:19px;line-height:20px;letter-spacing:.5px;text-transform:uppercase;width:150px;flex:none}
.main-nav{display:flex;gap:26px;margin-left:40px;font-size:12px;font-weight:500;letter-spacing:.4px;white-space:nowrap}
.header-icons{margin-left:auto;display:flex;gap:20px;align-items:center;flex:none}
.header-icons svg{width:24px;height:24px;stroke:var(--white);fill:none;stroke-width:2}

/* hero */
.hero{position:relative;height:568px;background:var(--paper);overflow:hidden}
.hero-dark{position:absolute;right:0;top:0;width:330px;height:100%;background:var(--black)}
.hero-copy{position:absolute;left:96px;top:112px;width:470px}
.hero-title{font-family:"Playfair Display",serif;font-weight:600;font-size:38px;line-height:48px;color:var(--ink)}
.hero-text{margin-top:20px;font-size:13px;line-height:21px;color:var(--muted);width:420px}
.btn{display:inline-flex;align-items:center;justify-content:center;border-radius:22px;font-size:13px;font-weight:500;height:40px;padding:0 28px;white-space:nowrap}
.btn-outline{border:1.5px solid var(--ink);color:var(--ink)}
.btn-solid{background:var(--ink);color:var(--white)}
.btn-light{border:1.5px solid var(--white);color:var(--white)}
.hero .btn{margin-top:26px}
.hero-photo{position:absolute;left:600px;top:68px;width:560px;height:420px;background:linear-gradient(135deg,#7d7a72,#3b3a36 55%,#1a1a1a)}

/* section titles */
.section-title{text-align:center;font-size:40px;font-weight:600;letter-spacing:1px;text-transform:uppercase}
.section-sub{text-align:center;font-size:13px;line-height:20px;color:var(--muted);width:620px;margin:10px auto 0}

/* popular */
.popular{height:788px;padding-top:70px}
.popular-grid{display:flex;gap:44px;justify-content:center;margin-top:96px}
.popular-card{width:320px;height:380px;border:1px solid var(--line);background:var(--white);box-shadow:0 6px 18px rgba(0,0,0,.08);text-align:center}
.popular-card .thumb{height:200px;margin:16px;background:linear-gradient(180deg,#f4f1ec,#d8cdbf)}
.card-title{font-size:15px;font-weight:600;text-transform:uppercase;margin-top:10px}
.card-desc{font-size:12.5px;line-height:18px;color:var(--muted);width:230px;margin:8px auto 0}
.popular-card .btn{height:34px;margin-top:12px;font-size:12px}

/* banner */
.banner{position:relative;height:320px;color:var(--white);text-align:center;overflow:hidden}
.banner-bg{position:absolute;inset:0;background:linear-gradient(90deg,#1b1b1b,#3c3c3c 50%,#1b1b1b)}
.banner-body{position:relative;padding-top:80px}
.banner .section-title{font-size:40px}
.banner .section-sub{color:#e3e3e3}
.banner-actions{display:flex;gap:30px;justify-content:center;margin-top:28px}
.banner-actions .btn{height:40px;width:148px;padding:0}

/* all products */
.products{height:832px;padding-top:76px}
.filters{display:flex;gap:14px;justify-content:center;margin-top:40px}
.filter{height:34px;padding:0 22px;border:1.5px solid #9a9a9a;border-radius:18px;font-size:13px;display:flex;align-items:center;color:#444;text-transform:uppercase;white-space:nowrap}
.filter.active{background:var(--ink);border-color:var(--ink);color:var(--white)}
.product-grid{display:flex;gap:28px;justify-content:center;margin-top:44px}
.product-card{width:332px}
.product-card .thumb-frame{position:relative;height:220px;border:1px solid var(--line);box-shadow:0 4px 14px rgba(0,0,0,.07);padding:14px}
.product-card .thumb{height:100%;background:linear-gradient(180deg,#f6f4f0,#cfc8bd)}
.heart{position:absolute;top:10px;right:12px;width:18px;height:18px;fill:var(--heart)}
.product-name{font-size:15px;font-weight:600;text-transform:uppercase;margin-top:16px}
.stars{display:flex;gap:2px;margin-top:6px}
.stars svg{width:13px;height:13px;fill:var(--star)}
.product-desc{font-size:12.5px;color:var(--muted);margin-top:6px}
.price{font-size:14px;font-weight:600;margin-top:4px}
.product-actions{display:flex;gap:12px;margin-top:12px}
.product-actions .btn{height:36px;width:120px;padding:0;font-size:13px}
.dots{display:flex;gap:7px;justify-content:center}
.dots span{width:8px;height:8px;border-radius:50%;background:#b9b9b9}
.dots span.on{background:var(--ink)}
.products .dots{margin-top:52px}

/* testimonials */
.testimonials{height:520px;background:var(--paper);padding-top:72px}
.review-grid{display:flex;gap:24px;justify-content:center;margin-top:52px}
.review-card{width:330px;height:280px;background:var(--white);box-shadow:0 4px 16px rgba(0,0,0,.08);text-align:center;padding-top:22px}
.avatar{width:64px;height:64px;border-radius:50%;margin:0 auto;background:linear-gradient(135deg,#c9a98e,#6f5444)}
.reviewer{font-size:15px;font-weight:600;margin-top:10px}
.role{font-size:12px;color:var(--muted);font-style:italic}
.review-card .stars{justify-content:center}
.review-text{font-size:12.5px;line-height:19px;color:var(--muted);width:260px;margin:12px auto 0}
.testimonials .dots{margin-top:34px}

/* footer */
.site-footer{height:440px;background:var(--black);color:var(--footer-text);display:flex;padding:92px 0 0 128px}
.footer-brand .brand{font-size:30px;line-height:34px;width:200px}
.socials{display:flex;gap:10px;margin-top:26px}
.socials span{width:34px;height:34px;border:2px solid var(--white);border-radius:50%}
.footer-col h4{font-size:18px;font-weight:500;color:var(--white);margin-bottom:22px}
.footer-col li{list-style:none;font-size:13px;margin-bottom:13px;display:flex;align-items:center;gap:10px}
.footer-col li svg{width:10px;height:10px;stroke:var(--white);fill:none;stroke-width:2}
.col-links{margin-left:30px;width:245px}
.col-services{width:178px}
.contact-item{display:flex;gap:14px;margin-bottom:18px;font-size:12.5px;line-height:18px}
.contact-item svg{width:20px;height:20px;fill:var(--white);flex:none;margin-top:2px}
.contact-item b{display:block;font-weight:500;font-size:12px;letter-spacing:.4px}
.bottom-bar{height:104px;background:#141414;color:var(--footer-text);display:flex;align-items:center;padding:0 72px 0 32px;font-size:13px}
.cards{margin-left:auto;display:flex;gap:8px}
.cards span{width:46px;height:30px;border-radius:4px;background:#e8e8e8}
.cards span:nth-child(2){background:#c9c9c9}
.cards span:nth-child(4){background:#bdbdbd}
</style>
</head>
<body>

<header class="site-header">
  <div class="brand">Ridgeback<br>Gear<br>Depot</div>
  <nav class="main-nav">
    <a href="#">AUDIO</a><a href="#">CANYON RUN</a><a href="#">POLAR RIDGE</a><a href="#">HONDO TRAIL</a><a href="#">KAZUMI</a><a href="#">HEIM/JOINTS</a><a href="#">SPACERS</a>
  </nav>
  <div class="header-icons">
    <svg viewBox="0 0 24 24"><circle cx="10" cy="10" r="7"/><path d="M15 15l6 6"/></svg>
    <svg viewBox="0 0 24 24"><path d="M2 3h3l3 12h11l3-9H7"/><circle cx="9" cy="20" r="1.5"/><circle cx="18" cy="20" r="1.5"/></svg>
    <svg viewBox="0 0 24 24"><circle cx="12" cy="12" r="10"/><circle cx="12" cy="10" r="3.5"/><path d="M5.5 19c2-3 11-3 13 0"/></svg>
  </div>
</header>

<section class="hero">
  <div class="hero-dark"></div>
  <div class="hero-copy">
    <h1 class="hero-title">Invest in Ridgeback Gear Depot With Affordable Price of Our Products</h1>
    <p class="hero-text">At all our showrooms you can enjoy a wet test that allows you to experience the healing power of a spa for yourself, to a service center and products on display.</p>
    <a class="btn btn-outline" href="#">Shop Here</a>
  </div>
  <div class="hero-photo" role="img" aria-label="Off-road side-by-side vehicle parked on a dark studio floor"></div>
</section>

<section class="popular">
  <h2 class="section-title">Most Popular Products</h2>
  <p class="section-sub">Lorem ipsum dolor sit amet, consectetur adipiscing elit, sed do eiusmod tempor incididunt ut viverra maecenas accumsan lacus vel facilisis.</p>
  <div class="popular-grid">
    <article class="popular-card">
      <div class="thumb" role="img" aria-label="Pair of brass rod end joints"></div>
      <h3 class="card-title">Rod End Supplier</h3>
      <p class="card-desc">Quarter Set of 1.25" Heims, Round Bungs &amp; Jam Nuts</p>
      <a class="btn btn-solid" href="#">Shop Now</a>
    </article>
    <article class="popular-card">
      <div class="thumb" role="img" aria-label="Set of rod ends with bungs and jam nuts"></div>
      <h3 class="card-title">Rod End Supplier</h3>
      <p class="card-desc">Quarter Set of 1.25" Heims, Round Bungs &amp; Jam Nuts</p>
      <a class="btn btn-solid" href="#">Shop Now</a>
    </article>
    <article class="popular-card">
      <div class="thumb" role="img" aria-label="Steel drive shaft with gear"></div>
      <h3 class="card-title">Rod End Supplier</h3>
      <p class="card-desc">Quarter Set of 1.25" Heims, Round Bungs &amp; Jam Nuts</p>
      <a class="btn btn-solid" href="#">Shop Now</a>
    </article>
  </div>
</section>

<section class="banner">
  <div class="banner-bg" role="img" aria-label="Close-up of engine parts in dark tones"></div>
  <div class="banner-body">
    <h2 class="section-title">Are You Looking for Ridgeback Gear Depot</h2>
    <p class="section-sub">Our best-selling RidgeFlow trail kits redefine the traditional off-road riding experience with powerful exercise and therapy features.</p>
    <div class="banner-actions">
      <a class="btn btn-light" href="#">Our Products</a>
      <a class="btn btn-light" href="#">Shop Now</a>
      <a class="btn btn-light" href="#">About Us</a>
    </div>
  </div>
</section>

<section class="products">
  <h2 class="section-title">All Products</h2>
  <p class="section-sub">Lorem ipsum dolor sit amet, consectetur adipiscing elit, sed do eiusmod tempor incididunt ut viverra maecenas accumsan lacus vel facilisis.</p>
  <div class="filters">
    <span class="filter active">All</span><span class="filter">Canyon Run</span><span class="filter">Polar Ridge</span><span class="filter">Hondo Trail</span><span class="filter">Kazumi</span><span class="filter">Heim/Joints</span><span class="filter">Spacers</span>
  </div>
  <div class="product-grid">
    <article class="product-card">
      <div class="thumb-frame">
        <div class="thumb" role="img" aria-label="Two chrome bushing spacers"></div>
        <svg class="heart" viewBox="0 0 24 24"><path d="M12 21l-1.5-1.3C5 15 2 12.2 2 8.5 2 5.4 4.4 3 7.5 3c1.7 0 3.4.8 4.5 2.1C13.1 3.8 14.8 3 16.5 3 19.6 3 22 5.4 22 8.5c0 3.7-3 6.5-8.5 11.2z"/></svg>
      </div>
      <h3 class="product-name">Verano Florence Patio</h3>
      <div class="stars"><svg viewBox="0 0 24 24"><path d="M12 2l3 7 7 .6-5.4 4.7 1.7 7.2L12 17.8 5.7 21.5l1.7-7.2L2 9.6 9 9z"/></svg><svg viewBox="0 0 24 24"><path d="M12 2l3 7 7 .6-5.4 4.7 1.7 7.2L12 17.8 5.7 21.5l1.7-7.2L2 9.6 9 9z"/></svg><svg viewBox="0 0 24 24"><path d="M12 2l3 7 7 .6-5.4 4.7 1.7 7.2L12 17.8 5.7 21.5l1.7-7.2L2 9.6 9 9z"/></svg><svg viewBox="0 0 24 24"><path d="M12 2l3 7 7 .6-5.4 4.7 1.7 7.2L12 17.8 5.7 21.5l1.7-7.2L2 9.6 9 9z"/></svg><svg viewBox="0 0 24 24"><path d="M12 2l3 7 7 .6-5.4 4.7 1.7 7.2L12 17.8 5.7 21.5l1.7-7.2L2 9.6 9 9z"/></svg></div>
      <p class="product-desc">Verano Florence Patio Swivel</p>
      <p class="price">$ 42.00</p>
      <div class="product-actions"><a class="btn btn-solid" href="#">Buy Now</a><a class="btn btn-outline" href="#">View Details</a></div>
    </article>
    <article class="product-card">
      <div class="thumb-frame">
        <div class="thumb" role="img" aria-label="Assorted rod ends and jam nuts"></div>
        <svg class="heart" viewBox="0 0 24 24"><path d="M12 21l-1.5-1.3C5 15 2 12.2 2 8.5 2 5.4 4.4 3 7.5 3c1.7 0 3.4.8 4.5 2.1C13.1 3.8 14.8 3 16.5 3 19.6 3 22 5.4 22 8.5c0 3.7-3 6.5-8.5 11.2z"/></svg>
      </div>
      <h3 class="product-name">Verano Catalina Patio</h3>
      <div class="stars"><svg viewBox="0 0 24 24"><path d="M12 2l3 7 7 .6-5.4 4.7 1.7 7.2L12 17.8 5.7 21.5l1.7-7.2L2 9.6 9 9z"/></svg><svg viewBox="0 0 24 24"><path d="M12 2l3 7 7 .6-5.4 4.7 1.7 7.2L12 17.8 5.7 21.5l1.7-7.2L2 9.6 9 9z"/></svg><svg viewBox="0 0 24 24"><path d="M12 2l3 7 7 .6-5.4 4.7 1.7 7.2L12 17.8 5.7 21.5l1.7-7.2L2 9.6 9 9z"/></svg><svg viewBox="0 0 24 24"><path d="M12 2l3 7 7 .6-5.4 4.7 1.7 7.2L12 17.8 5.7 21.5l1.7-7.2L2 9.6 9 9z"/></svg><svg viewBox="0 0 24 24"><path d="M12 2l3 7 7 .6-5.4 4.7 1.7 7.2L12 17.8 5.7 21.5l1.7-7.2L2 9.6 9 9z"/></svg></div>
      <p class="product-desc">AquaStride X500 Exercise System</p>
      <p class="price">$ 42.00</p>
      <div class="product-actions"><a class="btn btn-solid" href="#">Buy Now</a><a class="btn btn-outline" href="#">View Details</a></div>
    </article>
    <article class="product-card">
      <div class="thumb-frame">
        <div class="thumb" role="img" aria-label="Full kit of brass rod ends"></div>
        <svg class="heart" viewBox="0 0 24 24"><path d="M12 21l-1.5-1.3C5 15 2 12.2 2 8.5 2 5.4 4.4 3 7.5 3c1.7 0 3.4.8 4.5 2.1C13.1 3.8 14.8 3 16.5 3 19.6 3 22 5.4 22 8.5c0 3.7-3 6.5-8.5 11.2z"/></svg>
      </div>
      <h3 class="product-name">Verano Catalina Deep</h3>
      <div class="stars"><svg viewBox="0 0 24 24"><path d="M12 2l3 7 7 .6-5.4 4.7 1.7 7.2L12 17.8 5.7 21.5l1.7-7.2L2 9.6 9 9z"/></svg><svg viewBox="0 0 24 24"><path d="M12 2l3 7 7 .6-5.4 4.7 1.7 7.2L12 17.8 5.7 21.5l1.7-7.2L2 9.6 9 9z"/></svg><svg viewBox="0 0 24 24"><path d="M12 2l3 7 7 .6-5.4 4.7 1.7 7.2L12 17.8 5.7 21.5l1.7-7.2L2 9.6 9 9z"/></svg><svg viewBox="0 0 24 24"><path d="M12 2l3 7 7 .6-5.4 4.7 1.7 7.2L12 17.8 5.7 21.5l1.7-7.2L2 9.6 9 9z"/></svg><svg viewBox="0 0 24 24"><path d="M12 2l3 7 7 .6-5.4 4.7 1.7 7.2L12 17.8 5.7 21.5l1.7-7.2L2 9.6 9 9z"/></svg></div>
      <p class="product-desc">Verano Catalina Deep Seating Patio</p>
      <p class="price">$ 42.00</p>
      <div class="product-actions"><a class="btn btn-solid" href="#">Buy Now</a><a class="btn btn-outline" href="#">View Details</a></div>
    </article>
  </div>
  <div class="dots"><span class="on"></span><span></span><span></span><span></span><span></span></div>
</section>

<section class="testimonials">
  <h2 class="section-title">What Our Clients Says</h2>
  <div class="review-grid">
    <article class="review-card">
      <div class="avatar" role="img" aria-label="Portrait photo of the client"></div>
      <h3 class="reviewer">Marla Quinn</h3>
      <p class="role">Digitiser</p>
      <div class="stars"><svg viewBox="0 0 24 24"><path d="M12 2l3 7 7 .6-5.4 4.7 1.7 7.2L12 17.8 5.7 21.5l1.7-7.2L2 9.6 9 9z"/></svg><svg viewBox="0 0 24 24"><path d="M12 2l3 7 7 .6-5.4 4.7 1.7 7.2L12 17.8 5.7 21.5l1.7-7.2L2 9.6 9 9z"/></svg><svg viewBox="0 0 24 24"><path d="M12 2l3 7 7 .6-5.4 4.7 1.7 7.2L12 17.8 5.7 21.5l1.7-7.2L2 9.6 9 9z"/></svg><svg viewBox="0 0 24 24"><path d="M12 2l3 7 7 .6-5.4 4.7 1.7 7.2L12 17.8 5.7 21.5l1.7-7.2L2 9.6 9 9z"/></svg><svg viewBox="0 0 24 24"><path d="M12 2l3 7 7 .6-5.4 4.7 1.7 7.2L12 17.8 5.7 21.5l1.7-7.2L2 9.6 9 9z"/></svg></div>
      <p class="review-text">We don't place you into a loan profile each customer as an formula created by the banking industry.</p>
    </article>
    <article class="review-card">
      <div class="avatar" role="img" aria-label="Portrait photo of the client"></div>
      <h3 class="reviewer">Dana</h3>
      <p class="role">Digitiser</p>
      <div class="stars"><svg viewBox="0 0 24 24"><path d="M12 2l3 7 7 .6-5.4 4.7 1.7 7.2L12 17.8 5.7 21.5l1.7-7.2L2 9.6 9 9z"/></svg><svg viewBox="0 0 24 24"><path d="M12 2l3 7 7 .6-5.4 4.7 1.7 7.2L12 17.8 5.7 21.5l1.7-7.2L2 9.6 9 9z"/></svg><svg viewBox="0 0 24 24"><path d="M12 2l3 7 7 .6-5.4 4.7 1.7 7.2L12 17.8 5.7 21.5l1.7-7.2L2 9.6 9 9z"/></svg><svg viewBox="0 0 24 24"><path d="M12 2l3 7 7 .6-5.4 4.7 1.7 7.2L12 17.8 5.7 21.5l1.7-7.2L2 9.6 9 9z"/></svg><svg viewBox="0 0 24 24"><path d="M12 2l3 7 7 .6-5.4 4.7 1.7 7.2L12 17.8 5.7 21.5l1.7-7.2L2 9.6 9 9z"/></svg></div>
      <p class="review-text">We don't place you into a loan profile each customer as an formula created by the banking industry.</p>
    </article>
    <article class="review-card">
      <div class="avatar" role="img" aria-label="Portrait photo of the client"></div>
      <h3 class="reviewer">Bree</h3>
      <p class="role">Digitiser</p>
      <div class="stars"><svg viewBox="0 0 24 24"><path d="M12 2l3 7 7 .6-5.4 4.7 1.7 7.2L12 17.8 5.7 21.5l1.7-7.2L2 9.6 9 9z"/></svg><svg viewBox="0 0 24 24"><path d="M12 2l3 7 7 .6-5.4 4.7 1.7 7.2L12 17.8 5.7 21.5l1.7-7.2L2 9.6 9 9z"/></svg><svg viewBox="0 0 24 24"><path d="M12 2l3 7 7 .6-5.4 4.7 1.7 7.2L12 17.8 5.7 21.5l1.7-7.2L2 9.6 9 9z"/></svg><svg viewBox="0 0 24 24"><path d="M12 2l3 7 7 .6-5.4 4.7 1.7 7.2L12 17.8 5.7 21.5l1.7-7.2L2 9.6 9 9z"/></svg><svg viewBox="0 0 24 24"><path d="M12 2l3 7 7 .6-5.4 4.7 1.7 7.2L12 17.8 5.7 21.5l1.7-7.2L2 9.6 9 9z"/></svg></div>
      <p class="review-text">We don't place you into a loan profile each customer as an formula created by the banking industry.</p>
    </article>
  </div>
  <div class="dots"><span class="on"></span><span></span><span></span><span></span><span></span></div>
</section>

<footer class="site-footer">
  <div class="footer-brand">
    <div class="brand">Ridgeback<br>Gear<br>Depot</div>
    <div class="socials"><span></span><span></span><span></span></div>
  </div>
  <div class="footer-col col-links">
    <h4>Quick Links</h4>
    <ul>
      <li><svg viewBox="0 0 10 10"><path d="M3 1l4 4-4 4"/></svg>Home</li>
      <li><svg viewBox="0 0 10 10"><path d="M3 1l4 4-4 4"/></svg>About Us</li>
      <li><svg viewBox="0 0 10 10"><path d="M3 1l4 4-4 4"/></svg>Our Products</li>
      <li><svg viewBox="0 0 10 10"><path d="M3 1l4 4-4 4"/></svg>Clients Testimonials</li>
      <li><svg viewBox="0 0 10 10"><path d="M3 1l4 4-4 4"/></svg>Contact Us</li>
    </ul>
  </div>
  <div class="footer-col col-services">
    <h4>Services</h4>
    <ul>
      <li><svg viewBox="0 0 10 10"><path d="M3 1l4 4-4 4"/></svg>Audio</li>
      <li><svg viewBox="0 0 10 10"><path d="M3 1l4 4-4 4"/></svg>Canyon Run</li>
      <li><svg viewBox="0 0 10 10"><path d="M3 1l4 4-4 4"/></svg>Polar Ridge</li>
      <li><svg viewBox="0 0 10 10"><path d="M3 1l4 4-4 4"/></svg>Hondo Trail</li>
      <li><svg viewBox="0 0 10 10"><path d="M3 1l4 4-4 4"/></svg>Kazumi</li>
    </ul>
  </div>
  <div class="footer-col col-contact">
    <h4>Contact Us</h4>
    <div class="contact-item"><svg viewBox="0 0 24 24"><path d="M6.6 10.8a15 15 0 006.6 6.6l2.2-2.2c.3-.3.7-.4 1-.2 1.1.4 2.3.6 3.6.6.6 0 1 .4 1 1V20c0 .6-.4 1-1 1A17 17 0 013 4c0-.6.4-1 1-1h3.5c.6 0 1 .4 1 1 0 1.3.2 2.5.6 3.6.1.3 0 .7-.2 1z"/></svg><div><b>CALL US</b>(555) 014-2290</div></div>
    <div class="contact-item"><svg viewBox="0 0 24 24"><path d="M3 5h18v14H3z M3 5l9 7 9-7" fill="none" stroke="#fff" stroke-width="2"/></svg><div><b>EMAIL US</b>hello@ridgebackgeardepot.example</div></div>
    <div class="contact-item"><svg viewBox="0 0 24 24"><path d="M12 2a7 7 0 00-7 7c0 5 7 13 7 13s7-8 7-13a7 7 0 00-7-7zm0 9.5A2.5 2.5 0 1112 6a2.5 2.5 0 010 5.5z"/></svg><div>1280 Ridge Trail Rd, Cedar Bend, FL 32300</div></div>
  </div>
</footer>

<div class="bottom-bar">
  <p>All rights reserved, Copyrights @ 2024</p>
  <div class="cards"><span></span><span></span><span></span><span></span></div>
</div>

</body>
</html>
```